Business card design needed

Live music / DJ service

See my web site for ideas. www.darrenpikeevents.com.au

Some way of incorperating an electric guitar with a DJ
sound system might be good.
I'm really open to any ideas at this point.

I use a catch phrase "Hop2Jive" as I do most
of my work in Gladstone and Rockhampton.
The DJ service part is aimed mainly at weddings.

Reason: Still making up my mind

Industry/Entity Type

Business

Contact Information for Business Card

Mobile phone 0491 362817
email darren@darrenpikeevents.com.au

```html
<!DOCTYPE html>
<html lang="en">
<head>
<meta charset="utf-8">
<title>Hop 2 Jive – Business Card</title>
<link rel="stylesheet" href="https://fonts.googleapis.com/css2?family=Tinos:wght@400;700&display=swap">
<style>
  :root {
    --card-black: #000000;
    --ink-white: #ffffff;
    --label-blue: #6f8fc8;
    --photo-deep: #03060d;
    --photo-navy: #101d33;
    --photo-steel: #2c4468;
    --photo-ice: #9db6db;
    --photo-flash: #f4f7fc;
  }
  html, body {
    margin: 0;
    padding: 0;
    width: 1200px;
    height: 741px;
    overflow: hidden;
    background: var(--card-black);
  }
  .card {
    position: relative;
    width: 1200px;
    height: 741px;
    background: var(--card-black);
    overflow: hidden;
    font-family: "Tinos", "Times New Roman", serif;
    color: var(--ink-white);
  }
  .guitar-photo {
    position: absolute;
    left: 240px;
    top: 0;
    width: 960px;
    height: 741px;
    background:
      radial-gradient(ellipse 9% 12% at 40% 40%, var(--photo-flash), rgba(244,247,252,0.6) 35%, transparent 75%),
      radial-gradient(ellipse 26% 34% at 42% 48%, rgba(157,182,219,0.45), transparent 70%),
      radial-gradient(ellipse 10% 7% at 30% 78%, rgba(157,182,219,0.45), transparent 75%),
      linear-gradient(160deg, transparent 30%, rgba(157,182,219,0.28) 38%, transparent 46%),
      radial-gradient(ellipse 42% 30% at 78% 14%, rgba(157,182,219,0.5), rgba(44,68,104,0.5) 45%, transparent 80%),
      radial-gradient(ellipse 30% 40% at 90% 55%, rgba(44,68,104,0.75), transparent 80%),
      radial-gradient(ellipse 45% 30% at 82% 88%, rgba(44,68,104,0.85), rgba(16,29,51,0.6) 50%, transparent 85%),
      radial-gradient(ellipse 60% 70% at 70% 45%, var(--photo-navy), transparent 80%),
      var(--photo-deep);
    -webkit-mask-image: linear-gradient(to right, transparent 0%, #000 24%);
            mask-image: linear-gradient(to right, transparent 0%, #000 24%);
  }
  .catchphrase {
    position: absolute;
    left: 135px;
    top: 62px;
    margin: 0;
    font-size: 32px;
    font-weight: 400;
    letter-spacing: 0.16em;
    line-height: 1;
  }
  .brand-name {
    position: absolute;
    left: 117px;
    top: 318px;
    margin: 0;
    font-size: 104px;
    font-weight: 400;
    line-height: 1;
    color: var(--ink-white);
  }
  .contact {
    position: absolute;
    left: 143px;
    top: 612px;
    margin: 0;
    padding: 0;
    list-style: none;
    font-size: 28px;
    line-height: 48px;
  }
  .contact-label {
    color: var(--label-blue);
  }
  .contact-value {
    color: var(--ink-white);
  }
</style>
</head>
<body>
  <main class="card">
    <div class="guitar-photo" role="img" aria-label="Photograph of a black electric guitar lit in deep blue, with a bright white light-painted swirl across its body and the fretboard glowing at top right"></div>

    <p class="catchphrase">HOP 2 JIVE</p>

    <h1 class="brand-name">Hop2Jive</h1>

    <ul class="contact">
      <li><span class="contact-label">MOBILE PHONE</span> <span class="contact-value">0491 362817</span></li>
      <li><span class="contact-label">EMAIL</span> <span class="contact-value">DARREN@DARRENPIKEEVENTS.COM.AU</span></li>
    </ul>
  </main>
</body>
</html>
```